Spice Mix Label Bottle Branding - Health and Weight Loss Mixes

The company is called ZestRow Spice Mix's. We've created 5 spice mixes using ingredients that promote health and weight loss. We already have a logo but now we need labels for our bottles. We would like to see designs that have the feel of health supplements (see attached examples)

We would like a different colour featured with each of our flavours.

Our flavours are:
-Golden Chai (Yellow)
-Mild Curry (Orange)
-Coffee Rub (brown)
-Garlic Oregano (Green)
-Taco (Blue)

Thank you!

Target Market(s)

Ages 22-35. Men and Female. Trendy, Hipster.

Industry/Entity Type

Food Production

Font styles to use
Sans Serif

Colors
f37122
0655a3
0692cd
9bcb3c
fbee3f

Requirements
Must have
• A different featured colour for each flavour.
• The ZestRow Spices Logo (attached)
• The slogan: "Weight Loss Ingredients"
• -Golden Chai (Yellow)
• -Mild Curry (Orange)
• -Coffee Rub (brown)
• -Garlic Oregano (Green)
• -Taco (Blue)
• Text Files attached.
Nice to have
• A black label with a featured colour for each of the spice mice flavours.
• 'No Salt added'

```html
<!DOCTYPE html>
<html lang="en">
<head>
<meta charset="utf-8">
<title>ZestRow Spices – Flavour Labels</title>
<link href="https://fonts.googleapis.com/css2?family=Montserrat:wght@600;800&display=swap" rel="stylesheet">
<style>
  :root{
    --backdrop:#dcdcdc;
    --label-black:#0b0b0b;
    --ink-white:#ffffff;
    --curry:#f37122;
    --garlic:#9bcb3c;
    --coffee:#a4692e;
    --chai:#d9a21b;
    --taco:#0655a3;
  }
  *{margin:0;padding:0;box-sizing:border-box}
  html,body{width:1200px;height:923px;overflow:hidden;background:var(--backdrop)}
  .canvas{position:relative;width:1200px;height:923px;font-family:"Montserrat",sans-serif}
  .label{
    position:absolute;width:176px;height:172px;
    background:var(--label-black);color:var(--ink-white);
    display:flex;flex-direction:column;align-items:center;
    padding:12px 10px 10px;border-radius:4px;
    box-shadow:0 10px 24px rgba(0,0,0,.18);
  }
  .label--curry{left:172px;top:159px;--accent:var(--curry)}
  .label--garlic{left:849px;top:159px;--accent:var(--garlic)}
  .label--coffee{left:504px;top:354px;--accent:var(--coffee)}
  .label--chai{left:172px;top:649px;--accent:var(--chai)}
  .label--taco{left:849px;top:649px;--accent:var(--taco)}
  .label__mark{width:18px;height:18px;border-radius:50%;background:var(--accent)}
  .label__rule{position:relative;width:100%;height:1px;background:var(--accent);margin-top:4px}
  .label__rule::before,.label__rule::after{
    content:"";position:absolute;top:-1.5px;width:4px;height:4px;border-radius:50%;background:var(--accent)
  }
  .label__rule::before{left:0}
  .label__rule::after{right:0}
  .label__brand{
    margin-top:7px;font-weight:800;font-size:24px;line-height:1.02;
    letter-spacing:-0.6px;text-align:center;color:var(--ink-white);
  }
  .label__band{width:108px;height:4px;background:var(--accent);margin-top:6px}
  .label__slogan{margin-top:4px;font-weight:800;font-size:7px;letter-spacing:.1px;text-transform:uppercase}
  .label__dots{display:flex;gap:3px;margin-top:3px}
  .label__dots i{width:3px;height:3px;border-radius:50%;background:var(--accent)}
  .label__flavour{margin-top:3px;font-weight:800;font-size:16px;line-height:1.1;color:var(--accent);white-space:nowrap}
  .label__note{margin-top:3px;font-weight:600;font-size:7px}
</style>
</head>
<body>
<main class="canvas">
  <section class="label label--curry">
    <div class="label__mark"></div>
    <div class="label__rule"></div>
    <div class="label__brand">ZestRow<br>Spices</div>
    <div class="label__band"></div>
    <p class="label__slogan">Weight Loss Ingredients</p>
    <div class="label__dots"><i></i><i></i><i></i></div>
    <h2 class="label__flavour">Mild Curry</h2>
    <p class="label__note">No Salt added</p>
  </section>
  <section class="label label--garlic">
    <div class="label__mark"></div>
    <div class="label__rule"></div>
    <div class="label__brand">ZestRow<br>Spices</div>
    <div class="label__band"></div>
    <p class="label__slogan">Weight Loss Ingredients</p>
    <div class="label__dots"><i></i><i></i><i></i></div>
    <h2 class="label__flavour">Garlic Oregano</h2>
    <p class="label__note">No Salt added</p>
  </section>
  <section class="label label--coffee">
    <div class="label__mark"></div>
    <div class="label__rule"></div>
    <div class="label__brand">ZestRow<br>Spices</div>
    <div class="label__band"></div>
    <p class="label__slogan">Weight Loss Ingredients</p>
    <div class="label__dots"><i></i><i></i><i></i></div>
    <h2 class="label__flavour">Coffee Rub</h2>
    <p class="label__note">No Salt added</p>
  </section>
  <section class="label label--chai">
    <div class="label__mark"></div>
    <div class="label__rule"></div>
    <div class="label__brand">ZestRow<br>Spices</div>
    <div class="label__band"></div>
    <p class="label__slogan">Weight Loss Ingredients</p>
    <div class="label__dots"><i></i><i></i><i></i></div>
    <h2 class="label__flavour">Golden Chai</h2>
    <p class="label__note">No Salt added</p>
  </section>
  <section class="label label--taco">
    <div class="label__mark"></div>
    <div class="label__rule"></div>
    <div class="label__brand">ZestRow<br>Spices</div>
    <div class="label__band"></div>
    <p class="label__slogan">Weight Loss Ingredients</p>
    <div class="label__dots"><i></i><i></i><i></i></div>
    <h2 class="label__flavour">Taco</h2>
    <p class="label__note">No Salt added</p>
  </section>
</main>
</body>
</html>
```